Tallow Crest Business Card

We need a business card designed for a a company called "Tallow Crest". We offer consulting, coaching and training to business leaders and coaches (across the world) using the latest findings in neuroscience, social and emotional intelligence and positive psychology. The final design should communicate the use of brain science to create sustainable relationships.

The card should be doublesided. The logo is attached and names and titles will be provided to the successful designer. Thank you.

Industry/Entity Type

Training

```html
<!DOCTYPE html>
<html lang="en">
<head>
<meta charset="utf-8">
<title>Tallow Crest Business Card</title>
<link rel="stylesheet" href="https://fonts.googleapis.com/css2?family=Roboto:wght@400;500;700&display=swap">
<style>
  :root {
    --teal: #00c5c6;
    --teal-soft: #72e4e4;
    --white: #ffffff;
    --edge: #9a9a9a;
  }
  * { margin: 0; padding: 0; box-sizing: border-box; }
  html, body {
    width: 1200px;
    height: 936px;
    overflow: hidden;
    background: var(--white);
    font-family: "Roboto", Arial, sans-serif;
  }
  .sheet {
    position: relative;
    width: 1200px;
    height: 936px;
  }
  .card {
    position: absolute;
    top: 3px;
    width: 559px;
    height: 930px;
    border: 1.5px solid var(--edge);
    border-radius: 32px;
    overflow: hidden;
  }

  /* Front */
  .card-front {
    left: 3px;
    background: var(--teal);
  }
  .front-panel-shadow {
    position: absolute;
    left: 28px;
    top: 120px;
    width: 540px;
    height: 770px;
    border-radius: 120px 110px 130px 90px;
    background: var(--teal-soft);
  }
  .front-panel {
    position: absolute;
    left: 20px;
    top: 180px;
    width: 510px;
    height: 660px;
    border-radius: 100px 90px 120px 70px;
    background: var(--white);
  }
  .holder-name {
    position: absolute;
    left: 96px;
    top: 322px;
    font-size: 35px;
    font-weight: 400;
    letter-spacing: 0.5px;
    color: var(--teal);
  }
  .holder-role {
    position: absolute;
    left: 98px;
    top: 385px;
    font-size: 22px;
    font-weight: 500;
    color: var(--teal);
  }
  .contact-list {
    position: absolute;
    left: 104px;
    top: 506px;
    list-style: none;
    color: var(--teal);
    font-size: 26px;
  }
  .contact-list li {
    display: flex;
    height: 56px;
    align-items: center;
  }
  .contact-label { width: 38px; }
  .contact-sep { width: 88px; font-size: 20px; }
  .contact-row-mail .contact-sep { width: 38px; }

  /* Back */
  .card-back {
    left: 636px;
    background: var(--teal);
  }
  .back-band {
    position: absolute;
    left: 0;
    top: 0;
    width: 200px;
    height: 100%;
    background: var(--white);
  }
  .back-panel {
    position: absolute;
    left: 150px;
    top: 122px;
    width: 305px;
    height: 700px;
    border-radius: 0 150px 150px 0;
    background: var(--white);
  }
  .back-web {
    position: absolute;
    left: 52px;
    top: 248px;
    width: 0;
    height: 0;
  }
  .back-web span {
    position: absolute;
    left: 0;
    top: 0;
    transform: rotate(90deg);
    transform-origin: 0 0;
    white-space: nowrap;
    font-size: 29px;
    color: var(--teal);
    margin-left: 28px;
    margin-top: -3px;
    display: block;
    translate: 0 0;
  }
  .brand {
    position: absolute;
    left: 170px;
    top: 310px;
    width: 270px;
    text-align: center;
  }
  .brand-dot {
    display: block;
    width: 84px;
    height: 84px;
    margin: 0 auto 22px;
    border-radius: 50%;
    background: var(--teal);
  }
  .brand-name {
    font-size: 44px;
    font-weight: 700;
    line-height: 1.05;
    color: var(--teal);
  }
</style>
</head>
<body>
<main class="sheet">

  <section class="card card-front" aria-label="Card front">
    <div class="front-panel-shadow"></div>
    <div class="front-panel"></div>
    <h1 class="holder-name">YOUR NAME HERE</h1>
    <p class="holder-role">Position</p>
    <ul class="contact-list">
      <li><span class="contact-label">P</span><span class="contact-sep">:</span><span>+0012 34567891</span></li>
      <li><span class="contact-label">F</span><span class="contact-sep">:</span><span>+0012 34567891</span></li>
      <li class="contact-row-mail"><span class="contact-label">E</span><span class="contact-sep">:</span><span>www@www.w.com</span></li>
    </ul>
  </section>

  <section class="card card-back" aria-label="Card back">
    <div class="back-band"></div>
    <div class="back-panel"></div>
    <p class="back-web"><span>www@wwwwww.w.com</span></p>
    <div class="brand">
      <span class="brand-dot"></span>
      <p class="brand-name">Tallow<br>Crest</p>
    </div>
  </section>

</main>
</body>
</html>
```